LOGO DESIGN: Construction Related Service Business

We require a logo for our business Tovar Services. We are a construction related business offering a range of services including machine services for groundworks (digging trenches, soak wells, preparing land for construction etc), demolition and truck haulage from demolition sites.
We would like our logo to be predominately text, but may include abstract graphics. The colour scheme should be mainly a mid bright blue and overall be quite 'clean'.

Industry/Entity Type

Construction

Contact Information for Business Card

Dale Morrow
Ph:041 592 3068
tovarservices@quillnet.com.au

Colors
0456a3

```html
<!DOCTYPE html>
<html lang="en">
<head>
<meta charset="utf-8">
<title>Tovar Services — Business Card</title>
<link rel="stylesheet" href="https://fonts.googleapis.com/css2?family=Lato:wght@400;700&display=swap">
<style>
  :root {
    --backdrop: #8c8c8b;
    --card-stock: #e9e8dc;
    --brand-blue: #0456a3;
    --band-blue: #1a8fd3;
    --ink: #2b2b2b;
  }
  html, body {
    margin: 0;
    padding: 0;
    width: 1200px;
    height: 910px;
    overflow: hidden;
    background: var(--backdrop);
  }
  .canvas {
    position: relative;
    width: 1200px;
    height: 910px;
  }
  .business-card {
    position: absolute;
    left: 100px;
    top: 170px;
    width: 1000px;
    height: 570px;
    background: var(--card-stock);
    overflow: hidden;
    font-family: "Lato", Arial, sans-serif;
    color: var(--ink);
  }
  .side-band {
    position: absolute;
    left: 0;
    top: 0;
    width: 165px;
    height: 100%;
    background: var(--band-blue);
  }
  .holder-name {
    position: absolute;
    right: 80px;
    top: 40px;
    margin: 0;
    font-size: 34px;
    font-weight: 700;
  }
  .brand-lockup {
    position: absolute;
    left: 320px;
    top: 175px;
    display: flex;
    align-items: center;
    gap: 18px;
  }
  .brand-dot {
    width: 62px;
    height: 62px;
    border-radius: 50%;
    background: var(--band-blue);
    flex: none;
  }
  .brand-name {
    margin: 0;
    font-size: 50px;
    font-weight: 700;
    letter-spacing: 0.5px;
    text-transform: uppercase;
    color: var(--brand-blue);
    white-space: nowrap;
  }
  .contact-details {
    position: absolute;
    left: 440px;
    top: 360px;
    width: 420px;
    text-align: center;
    font-size: 22px;
    line-height: 1.45;
  }
  .contact-details p { margin: 0; }
</style>
</head>
<body>
  <main class="canvas">
    <section class="business-card">
      <div class="side-band"></div>
      <h1 class="holder-name">Dale Morrow</h1>
      <div class="brand-lockup">
        <span class="brand-dot"></span>
        <p class="brand-name">Tovar Services</p>
      </div>
      <div class="contact-details">
        <p class="contact-phone">Phone : + 041 592 3068</p>
        <p class="contact-email">tovarservices@quillnet.com.au</p>
      </div>
    </section>
  </main>
</body>
</html>
```